Graphic lion print design with text

I like the gold effects in image 2 as described in my attached document, but i'm open to other suggestions. The desired image is image 1. This is a gift for a Leo friend. This is going to be printed and framed to be hung on the wall in a large frame, in landscape format. I like the idea of using different font styles to separate the statements.

• I’m open to the suggestions about the font styles, but I want to separate the statements by using different font styles as shown in attached document.
Must be landscape format.
Small fonts preferred, as shown in the attached image.
• I like the gold effect in image 2 but other suggestions/colours welcome
• Please don't stretch the picture so I can have a good resolution. Place the text on another black background template and then paste the picture beside to the text.

```html
<!DOCTYPE html>
<html lang="en">
<head>
<meta charset="utf-8">
<title>Lion Blessing Print</title>
<link rel="stylesheet" href="https://fonts.googleapis.com/css2?family=Dancing+Script:wght@700&family=Federo&family=Crimson+Text&family=Montserrat:wght@700&family=Open+Sans:wght@600;700&family=Almendra&family=Advent+Pro:wght@400&display=swap">
<style>
  :root {
    --gold: #fcc30d;
    --gold-deep: #b8860b;
    --gold-dark: #5a3d05;
    --ink: #000000;
    --outer: #0b0b0b;
  }
  html, body {
    margin: 0;
    padding: 0;
    width: 1200px;
    height: 1025px;
    overflow: hidden;
    background: var(--outer);
  }
  .poster {
    position: relative;
    width: 1200px;
    height: 1025px;
    background: var(--outer);
  }
  .frame {
    position: absolute;
    left: 25px;
    top: 22px;
    width: 1128px;
    height: 960px;
    border: 10px solid var(--gold);
    background: var(--ink);
    overflow: hidden;
  }
  .lion-art {
    position: absolute;
    left: 670px;
    top: 70px;
    width: 470px;
    height: 900px;
    background:
      radial-gradient(ellipse 55% 45% at 72% 52%, #c8901a 0%, #8a5a0c 40%, rgba(90,61,5,0.5) 65%, rgba(0,0,0,0) 85%),
      radial-gradient(ellipse 60% 50% at 60% 30%, rgba(252,195,13,0.45) 0%, rgba(0,0,0,0) 70%);
  }
  .line {
    position: absolute;
    left: 0;
    width: 100%;
    text-align: center;
    color: var(--gold);
    white-space: nowrap;
    transform: translateY(-50%);
    margin: 0;
    line-height: 1.1;
  }
  .col-wide { left: 72px; width: 866px; }
  .col-main { left: 40px; width: 730px; }
  .script { font-family: 'Dancing Script', cursive; font-weight: 700; }
  .deco { font-family: 'Federo', sans-serif; }
  .serif { font-family: 'Crimson Text', serif; }
  .bold-sans { font-family: 'Montserrat', sans-serif; font-weight: 700; }
  .semi-sans { font-family: 'Open Sans', sans-serif; font-weight: 700; }
  .medieval { font-family: 'Almendra', serif; }

  .headline { top: 52px; font-size: 32px; }
  .tag-box {
    position: absolute;
    left: 305px;
    top: 87px;
    width: 356px;
    height: 52px;
    border: 2px solid var(--gold);
    box-sizing: border-box;
    color: var(--gold);
    font-family: 'Federo', sans-serif;
    font-size: 30px;
    display: flex;
    align-items: center;
    justify-content: center;
  }
  .conqueror { top: 168px; font-size: 28px; }
  .divider {
    position: absolute;
    height: 3px;
    background: linear-gradient(90deg, rgba(252,195,13,0), var(--gold) 50%, rgba(252,195,13,0));
  }
  .divider-1 { left: 222px; top: 196px; width: 525px; }
  .almighty { top: 250px; font-size: 32px; left: 40px; width: 650px; }
  .come-through { top: 306px; font-size: 31px; }
  .seek { top: 361px; font-size: 40px; }
  .trouble { top: 412px; font-size: 28px; }
  .divider-2 { left: 108px; top: 445px; width: 532px; }
  .may-god { top: 484px; font-size: 30px; }
  .calm { top: 526px; font-size: 31px; }
  .amp { top: 567px; font-size: 30px; }
  .still { top: 609px; font-size: 30px; }
  .divider-3 { left: 120px; top: 642px; width: 512px; }
  .doors { top: 675px; font-size: 30px; }
  .open { top: 716px; font-size: 33px; }
  .places { top: 760px; font-size: 27px; }

  .promise-box {
    position: absolute;
    left: 59px;
    top: 794px;
    width: 828px;
    height: 145px;
    border: 2px solid var(--gold);
    box-sizing: border-box;
    color: var(--gold);
    font-family: 'Advent Pro', sans-serif;
    font-size: 33px;
    line-height: 41px;
    text-align: center;
    padding-top: 9px;
  }
  .promise-box p { margin: 0; }
</style>
</head>
<body>
<div class="poster">
  <div class="frame">
    <div class="lion-art" role="img" aria-label="Roaring lion head in profile rendered in gold dust particles, dispersing to the left"></div>

    <p class="line col-wide script headline">It doesn't matter who or what may come against you</p>
    <div class="tag-box">FOR GOD IS WITH YOU</div>
    <p class="line col-wide serif conqueror">HE has made you more than a conqueror.</p>
    <div class="divider divider-1"></div>

    <p class="line script almighty">Almighty GOD</p>
    <p class="line col-main bold-sans come-through">will come through for you</p>
    <p class="line col-main script seek">when you Seek Him</p>
    <p class="line col-main semi-sans trouble">in your moments of trouble &amp; unrest</p>
    <div class="divider divider-2"></div>

    <p class="line col-main deco may-god">MAY GOD</p>
    <p class="line col-main medieval calm">calm the restlessness of your mind</p>
    <p class="line col-main bold-sans amp">&amp;</p>
    <p class="line col-main bold-sans still">still the thouhgts that worry you.</p>
    <div class="divider divider-3"></div>

    <p class="line col-main bold-sans doors">DOORS</p>
    <p class="line col-main serif open">will open for you,</p>
    <p class="line col-main semi-sans places">in the most unlikeliest of places.</p>

    <div class="promise-box">
      <p>When you go through deep waters, He will be with you.</p>
      <p>Never will He leave you, Never will He forsake you.</p>
      <p>Amen.</p>
    </div>
  </div>
</div>
</body>
</html>
```